Kolmar Foods needs a new label for canned pineapple

We want a very tasty (in terms of making your mouth water) and clean design (less is more) for our canned pineapple under the new logo of Kolmar Leafs division

Target Market(s)

The company’s mission is to bring quality food to target audiences of any social status (you receive a bit more than what you spend). Our core values are: reliability, loyalty and commitment to development.
The product is sold to mainstream and lower Mainstream customers.

Requirements
Must have
• The design should take into consideration the visibility on the shelf among competitor products (brief file) and that the product is a MAINSTREAM product.
We want a very tasty (in terms of making your mouth water) and clean design (less is more). The design should be easily modifiable for other canned fruits or vegetables.
The package must display on the front the following elements listed in the order of their should have noticeability:
• Kolmar Leaf logo
• Pineapple picture
• Product name
Designers should take into account that the shelfs for displaying the products in the shops may have an elevation of up to 3 cm that can overlap the product label.

Guidelines
• We would like the packaging to be as simple as possible (or at least not to sabotage the Kolmar name ), as our strategy depends on the agressive communication of the Kolmar logo.
• We would also like to communicate through suggestive and optimal colours as to be easily spotted on the shelf.
• As we have quite a minimal communication budget we need basically for the packaging to do a lot of the communication job itself
• FMCG is a highly visual industry so we have to include pictures of the products on the packages (even more than others do, as we are focused on health and quality - we want people to have that feeling of fresh products even though we are selling canned ones)
Should not have
• but the minimum amount of text on the front.

```html
<!DOCTYPE html>
<html lang="en">
<head>
<meta charset="utf-8">
<title>Kolmar Leafs – Pineapple Broken Slices label</title>
<link rel="stylesheet" href="https://fonts.googleapis.com/css2?family=Nunito:wght@800;900&display=swap">
<style>
  :root {
    --page: #ffffff;
    --sky: #3ba9cc;
    --sky-deep: #2b8fb3;
    --sun: #f7d21c;
    --sun-deep: #f0b90f;
    --lime: #b9d94a;
    --leaf: #1e7a34;
    --title: #e8901c;
    --title-edge: #7a3f08;
    --fruit-light: #fdf1bd;
    --fruit-mid: #f3d36a;
    --fruit-deep: #c9962e;
    --crown: #6f8f3a;
    --rind: #b07a26;
  }
  html, body {
    margin: 0;
    width: 1200px;
    height: 1200px;
    overflow: hidden;
    background: var(--page);
  }
  .canvas {
    position: relative;
    width: 1200px;
    height: 1200px;
  }
  .label {
    position: absolute;
    left: 250px;
    top: 150px;
    width: 700px;
    height: 900px;
    overflow: hidden;
  }
  .label-art {
    position: absolute;
    inset: 0;
    width: 700px;
    height: 900px;
  }
  .brand {
    position: absolute;
    top: 150px;
    left: 0;
    right: 0;
    display: flex;
    justify-content: center;
    align-items: center;
    gap: 18px;
  }
  .brand-mark {
    width: 54px;
    height: 54px;
    border-radius: 50%;
    background: var(--leaf);
  }
  .brand-name {
    font-family: "Nunito", sans-serif;
    font-weight: 900;
    font-size: 76px;
    color: var(--leaf);
    line-height: 1;
  }
  .product-name {
    position: absolute;
    top: 318px;
    left: 0;
    right: 0;
    margin: 0;
    text-align: center;
    font-family: "Nunito", sans-serif;
    font-weight: 900;
    text-transform: uppercase;
    color: var(--title);
    line-height: 0.92;
    -webkit-text-stroke: 3px var(--title-edge);
    paint-order: stroke fill;
  }
  .product-name .line-main { display: block; font-size: 100px; letter-spacing: 1px; }
  .product-name .line-sub  { display: block; font-size: 62px; letter-spacing: 1px; }
  .product-variant {
    position: absolute;
    top: 498px;
    left: 0;
    right: 0;
    margin: 0;
    text-align: center;
    font-family: "Nunito", sans-serif;
    font-weight: 900;
    font-size: 40px;
    line-height: 1;
    text-transform: uppercase;
    color: var(--leaf);
    letter-spacing: 1px;
  }
</style>
</head>
<body>
<main class="canvas">
  <section class="label">
    <svg class="label-art" viewBox="0 0 700 900" xmlns="http://www.w3.org/2000/svg">
      <defs>
        <radialGradient id="chunkTone" cx="0.6" cy="0.45" r="0.7">
          <stop offset="0" stop-color="var(--fruit-light)"/>
          <stop offset="0.55" stop-color="var(--fruit-mid)"/>
          <stop offset="1" stop-color="var(--fruit-deep)"/>
        </radialGradient>
        <linearGradient id="wholeTone" x1="0" y1="0" x2="0" y2="1">
          <stop offset="0" stop-color="var(--crown)"/>
          <stop offset="0.4" stop-color="var(--rind)"/>
          <stop offset="1" stop-color="var(--sun-deep)"/>
        </linearGradient>
      </defs>
      <rect class="label-ground" width="700" height="900" fill="var(--sky)"/>
      <rect class="top-band" y="28" width="700" height="20" fill="var(--sun)"/>
      <rect class="top-band-thin" y="62" width="700" height="8" fill="var(--sun-deep)"/>
      <path class="wave-sun" fill="var(--sun)"
        d="M0 300 C90 270 170 320 260 295 C350 270 430 320 520 292 C600 268 650 300 700 285 L700 900 L0 900 Z"/>
      <path class="wave-lime" fill="var(--lime)"
        d="M0 470 C80 445 150 490 240 470 C330 450 420 495 510 472 C590 452 650 480 700 468 L700 900 L0 900 Z"/>
      <path class="wave-sun-mid" fill="var(--sun)"
        d="M0 488 C90 468 170 505 260 488 C350 470 440 508 530 490 C610 474 660 498 700 488 L700 900 L0 900 Z"/>
      <path class="wave-sky" fill="var(--sky-deep)"
        d="M0 560 C90 540 170 580 260 562 C350 545 440 582 530 564 C610 548 660 572 700 562 L700 900 L0 900 Z"/>
      <path class="wave-sun-low" fill="var(--sun-deep)"
        d="M0 585 C90 565 170 600 260 585 C350 570 440 605 530 588 C610 572 660 595 700 585 L700 900 L0 900 Z"/>
      <g class="fruit-photo" role="img" aria-label="Photograph of a whole pineapple with a cut ring beside a heap of golden pineapple chunks in syrup">
        <path fill="url(#chunkTone)"
          d="M0 620 C60 600 110 640 180 615 C250 592 300 640 370 612 C440 590 500 635 570 608 C630 590 670 612 700 604 L700 900 L0 900 Z"/>
        <ellipse cx="120" cy="760" rx="110" ry="130" fill="url(#wholeTone)" opacity="0.85"/>
      </g>
    </svg>

    <div class="brand">
      <span class="brand-mark"></span>
      <span class="brand-name">Kolmar Leafs</span>
    </div>

    <h1 class="product-name">
      <span class="line-main">Pineapple</span>
      <span class="line-sub">Broken Slices</span>
    </h1>
    <p class="product-variant">In Light Syrup</p>
  </section>
</main>
</body>
</html>
```